BRAMBLE CABS

Taxi card design

Need changes very slow in replying to my messages.

Target Market(s)

Customers

Industry/Entity Type

Taxi

Contact Information for Business Card

See previous design

Font styles to use
Sans Serif

Colors
A7469A
B969AE
D3A5CF
EDDBEB
F8F0F9
6B429C
8869AF
B7A5CE
E3DAEB
F3F0F8

Requirements
Nice to have
• We are in the business of looking after people, not just driving vehicles front
Should not have
• Front number 01832 419 526 needs to big big

```html
<!DOCTYPE html>
<html lang="en">
<head>
<meta charset="utf-8">
<title>Bramble Cabs – Business Card</title>
<link rel="stylesheet" href="https://fonts.googleapis.com/css2?family=Saira+Semi+Condensed:wght@500;600;700&display=swap">
<style>
  :root {
    --plum: #A7469A;
    --violet: #6B429C;
    --violet-deep: #653F86;
    --ink: #111111;
    --paper: #FFFFFF;
    --backdrop: #CCCCCC;
  }
  * { box-sizing: border-box; margin: 0; padding: 0; }
  html, body { width: 1096px; height: 1200px; overflow: hidden; }
  body {
    background: var(--backdrop);
    font-family: "Saira Semi Condensed", "Arial Narrow", Arial, sans-serif;
    color: var(--ink);
    position: relative;
  }
  .card {
    position: absolute;
    left: 76px;
    width: 943px;
    height: 539px;
    overflow: hidden;
  }
  .card-front { top: 45px; background: var(--paper); }
  .card-back {
    top: 615px;
    background: linear-gradient(180deg, var(--plum) 0%, var(--violet-deep) 100%);
  }
  .brand-name {
    position: absolute;
    font-weight: 700;
    letter-spacing: 1px;
    white-space: nowrap;
    line-height: 1;
  }
  .card-front .brand-name {
    left: 33px; top: 60px;
    font-size: 56px;
    color: var(--plum);
  }
  .established {
    position: absolute;
    left: 54px; top: 140px;
    font-size: 21px; font-weight: 600;
    white-space: nowrap;
  }
  .service-hours {
    position: absolute;
    left: 290px; top: 158px;
    font-size: 32px; font-weight: 600;
    line-height: 1.1;
    white-space: nowrap;
  }
  .services {
    position: absolute;
    left: 540px; top: 32px;
    width: 380px;
    text-align: center;
    list-style: none;
    font-size: 30px; font-weight: 600;
    line-height: 47px;
    letter-spacing: 0.5px;
    white-space: nowrap;
  }
  .main-phone {
    position: absolute;
    display: flex; align-items: center;
    gap: 14px;
    font-weight: 600;
    font-size: 52px;
    line-height: 1;
    white-space: nowrap;
  }
  .card-front .main-phone { left: 274px; top: 224px; }
  .phone-icon { width: 48px; height: 48px; flex: none; }
  .phone-pills {
    position: absolute;
    left: 34px; top: 298px;
    display: flex; gap: 29px;
  }
  .phone-pill {
    width: 273px; height: 59px;
    border-radius: 22px 22px 0 22px;
    background: linear-gradient(180deg, var(--plum) 0%, var(--violet) 100%);
    color: var(--paper);
    display: flex; align-items: center; justify-content: center;
    gap: 10px;
    font-size: 29px; font-weight: 600;
    white-space: nowrap;
  }
  .phone-pill .phone-icon { width: 28px; height: 28px; }
  .contact-details, .address {
    position: absolute;
    top: 374px;
    font-size: 24px; font-weight: 600;
    line-height: 36.5px;
    font-style: normal;
    white-space: nowrap;
  }
  .contact-details { left: 34px; }
  .address { left: 624px; }
  .card-back .brand-name {
    left: 0; right: 0; top: 185px;
    text-align: center;
    font-size: 88px;
    color: var(--paper);
  }
  .card-back .main-phone {
    left: 0; right: 0; top: 332px;
    justify-content: center;
    color: var(--paper);
  }
</style>
</head>
<body>

<section class="card card-front" aria-label="Business card front">
  <div class="brand-name">BRAMBLE CABS</div>
  <div class="established">Established since 1986</div>
  <div class="service-hours">24/7 Service</div>

  <ul class="services">
    <li>AIRPORT TRANSFERS</li>
    <li>MINIBUSES</li>
    <li>SCHOOL TRANSPORT</li>
  </ul>

  <div class="main-phone">
    <svg class="phone-icon" viewBox="0 0 48 48" aria-hidden="true">
      <rect width="48" height="48" rx="7" fill="#111"/>
      <path d="M17 11c-2 0-5 3-5 6 0 10 9 20 19 20 3 0 6-3 6-5l-6-5-3 3c-3-1-7-5-8-8l3-3-6-8z" fill="#fff"/>
    </svg>
    <span>01832 419 526</span>
  </div>

  <div class="phone-pills">
    <div class="phone-pill">
      <svg class="phone-icon" viewBox="0 0 48 48" aria-hidden="true">
        <rect width="48" height="48" rx="7" fill="#fff"/>
        <path d="M17 11c-2 0-5 3-5 6 0 10 9 20 19 20 3 0 6-3 6-5l-6-5-3 3c-3-1-7-5-8-8l3-3-6-8z" fill="#A7469A"/>
      </svg>
      <span>01832 41 55 55</span>
    </div>
    <div class="phone-pill">
      <svg class="phone-icon" viewBox="0 0 48 48" aria-hidden="true">
        <rect width="48" height="48" rx="7" fill="#fff"/>
        <path d="M17 11c-2 0-5 3-5 6 0 10 9 20 19 20 3 0 6-3 6-5l-6-5-3 3c-3-1-7-5-8-8l3-3-6-8z" fill="#A7469A"/>
      </svg>
      <span>01832 30 30 30</span>
    </div>
    <div class="phone-pill">
      <svg class="phone-icon" viewBox="0 0 48 48" aria-hidden="true">
        <rect width="48" height="48" rx="7" fill="#fff"/>
        <path d="M17 11c-2 0-5 3-5 6 0 10 9 20 19 20 3 0 6-3 6-5l-6-5-3 3c-3-1-7-5-8-8l3-3-6-8z" fill="#A7469A"/>
      </svg>
      <span>01832 41 77 22</span>
    </div>
  </div>

  <div class="contact-details">
    <p>Freephone: 0800 555 0 147</p>
    <p>Email: bramblecabs@mailbox.co.uk</p>
    <p>Website: www.bramblecabs.co.uk</p>
  </div>

  <address class="address">
    Holly Lane Church Hall<br>
    Orchard St<br>
    Thornbury<br>
    TB14 6QK
  </address>
</section>

<section class="card card-back" aria-label="Business card back">
  <div class="brand-name">BRAMBLE CABS</div>
  <div class="main-phone">
    <svg class="phone-icon" viewBox="0 0 48 48" aria-hidden="true">
      <rect width="48" height="48" rx="7" fill="#fff"/>
      <path d="M17 11c-2 0-5 3-5 6 0 10 9 20 19 20 3 0 6-3 6-5l-6-5-3 3c-3-1-7-5-8-8l3-3-6-8z" fill="#8A4498"/>
    </svg>
    <span>01832 419 526</span>
  </div>
</section>

</body>
</html>
```